Thornwick auto buffing and headlight restoration

I'm offering a service the will restore dull and discoloured headlights caused by sun damage. I also want to offer minor scratch repairs. $25 per headlight $10-$30 for scratches Mobile serviceI'd like to have an example of a dull and a new headlight. Clean colours eg. Blues,silver and whites.Very clean uncomplicated and professionals looking card. I'd like it to have a bold logo.

Target Market(s)

All car, truck and vehicle owners. Automotive industries.

Industry/Entity Type

Automotive

Contact Information for Business Card

(Front)
Headlight restoration and scratch Repair
Callum Thornwick
Mobile-0412 386 904
(Back)
Pricing
$25 per headlight
$10-$35 per scratch

Font styles to use
Sans Serif

Colors
85cae6
ffffff
0355a3
faa54b

Requirements
Must have
• Logo
• I would like my name to look confident. As if to say "I back myself"
• Bold easy to read text
• Clean lines
• Name -Callum Thornwick
• Phone- txt or call 0412386904
• Email- 47calt@mailverno.com
Nice to have
• I'm open to other color schemes
• 4 color scheme only
• Minimal orange
• Small amount of Silver if possible
• Bold outlined logo
Should not have
• Complex lines and logos

```html
<!DOCTYPE html>
<html lang="en">
<head>
<meta charset="utf-8">
<title>Callum Thornwick – Business Card</title>
<link rel="stylesheet" href="https://fonts.googleapis.com/css2?family=Lato:wght@300;400;700&display=swap">
<style>
  :root {
    --backdrop: #151516;
    --backdrop-edge: #0c0c0d;
    --card: #2f3033;
    --card-line: #34353a;
    --orange: #faa54b;
    --white: #f2f2f2;
  }
  * { margin: 0; padding: 0; box-sizing: border-box; }
  html, body {
    width: 1200px;
    height: 900px;
    overflow: hidden;
  }
  body {
    position: relative;
    background: radial-gradient(ellipse at center, var(--backdrop) 0%, var(--backdrop-edge) 100%);
    font-family: "Lato", Arial, sans-serif;
  }
  .card {
    position: absolute;
    left: 320px;
    width: 560px;
    height: 328px;
    background:
      repeating-linear-gradient(90deg, var(--card) 0 2px, var(--card-line) 2px 3px);
    background-color: var(--card);
  }
  .card--front { top: 116px; }
  .card--back  { top: 483px; }

  .brand {
    position: absolute;
    display: flex;
    flex-direction: column;
    align-items: center;
    color: var(--orange);
    font-weight: 700;
    text-align: center;
  }
  .brand__dot {
    border-radius: 50%;
    background: var(--orange);
  }
  .brand__name { line-height: 1.15; }

  .card--front .brand { left: 52px; top: 100px; width: 212px; }
  .card--front .brand__dot { width: 80px; height: 80px; margin-bottom: 10px; }
  .card--front .brand__name { font-size: 21px; }
  .card--front .brand__sub { font-size: 14px; }

  .card--back .brand { left: 160px; top: 84px; width: 240px; }
  .card--back .brand__dot { width: 88px; height: 88px; margin-bottom: 10px; }
  .card--back .brand__name { font-size: 23px; }
  .card--back .brand__sub { font-size: 15px; }

  .contact {
    position: absolute;
    left: 299px;
    top: 122px;
  }
  .contact__name {
    color: var(--orange);
    font-size: 24px;
    font-weight: 400;
    letter-spacing: 0.2px;
  }
  .contact__phone {
    margin-top: 4px;
    color: var(--white);
    font-size: 14px;
  }

  .pricing {
    position: absolute;
    left: 0;
    right: 0;
    top: 260px;
    text-align: center;
    color: var(--orange);
    font-size: 17px;
  }
</style>
</head>
<body>
  <section class="card card--front">
    <div class="brand">
      <span class="brand__dot"></span>
      <span class="brand__name">Headlight Restoration</span>
      <span class="brand__sub">&amp; Scratch Repair</span>
    </div>
    <div class="contact">
      <p class="contact__name">Callum Thornwick</p>
      <p class="contact__phone">Mobile-0412 386 904</p>
    </div>
  </section>

  <section class="card card--back">
    <div class="brand">
      <span class="brand__dot"></span>
      <span class="brand__name">Headlight Restoration</span>
      <span class="brand__sub">&amp; Scratch Repair</span>
    </div>
    <p class="pricing">Pricing $25 per headlight $10-$35 per scratch</p>
  </section>
</body>
</html>
```